Stationary Design using supplied logo

24 Hour Completion required after acceptance

Business Cards
Letter Head
With Compliments Slips
Web Page Theme

Please only use a the following colors:

Red
Charcoal
Chrome/Silver
White

Red being the DOMINANT Color

Please email questions you may have.

Continued work available to suitably motivated designer.

Industry/Entity Type

Business

```html
<!DOCTYPE html>
<html lang="en">
<head>
<meta charset="utf-8">
<title>Lark Funds – Business Card</title>
<link href="https://fonts.googleapis.com/css2?family=Montserrat:wght@300;400;600;700&display=swap" rel="stylesheet">
<style>
  :root {
    --red: #b8202e;
    --charcoal: #3d3e40;
    --charcoal-deep: #353638;
    --silver: #e9eaec;
    --white: #ffffff;
    --text: #3a3a3c;
    --backdrop: #e4e6ea;
  }
  * { margin: 0; padding: 0; box-sizing: border-box; }
  html, body { width: 1200px; height: 934px; overflow: hidden; }
  body {
    background: radial-gradient(ellipse at 50% 40%, #f3f4f6 0%, var(--backdrop) 100%);
    font-family: "Montserrat", sans-serif;
    color: var(--text);
    position: relative;
  }
  .card {
    position: absolute;
    width: 600px;
    height: 350px;
    border-radius: 4px;
    overflow: hidden;
    box-shadow: 0 10px 26px rgba(0,0,0,.14);
  }
  /* back of card */
  .card--back {
    left: 90px; top: 110px;
    background: var(--charcoal);
  }
  .card--back .faint-disc {
    position: absolute;
    left: 80px; top: -40px;
    width: 360px; height: 360px;
    border-radius: 50%;
    background: var(--charcoal-deep);
  }
  .brand {
    position: absolute;
    display: flex;
    align-items: center;
    gap: 14px;
  }
  .brand__name {
    font-weight: 300;
    font-size: 58px;
    letter-spacing: 1px;
    line-height: 1;
  }
  .brand__dot {
    width: 34px; height: 34px;
    border-radius: 50%;
    background: var(--red);
  }
  .tagline {
    position: absolute;
    font-weight: 600;
    font-size: 14px;
    letter-spacing: 5px;
  }
  .card--back .brand { left: 150px; top: 120px; }
  .card--back .brand__name { color: var(--white); }
  .card--back .tagline { left: 168px; top: 196px; color: var(--white); }

  /* front of card */
  .card--front {
    left: 520px; top: 470px;
    background: linear-gradient(135deg, var(--white) 0%, #f4f5f6 100%);
  }
  .card--front .faint-disc {
    position: absolute;
    right: -30px; top: -50px;
    width: 220px; height: 220px;
    border-radius: 50%;
    background: var(--silver);
    opacity: .6;
  }
  .card--front .brand { left: 40px; top: 56px; }
  .card--front .brand__name { color: var(--text); }
  .card--front .tagline { left: 58px; top: 132px; color: var(--text); }

  .person { position: absolute; left: 58px; top: 196px; }
  .person__name {
    color: var(--red);
    font-weight: 700;
    font-size: 17px;
    letter-spacing: .5px;
  }
  .person__creds { font-size: 12px; font-weight: 400; color: var(--text); margin-left: 4px; letter-spacing: 0; }
  .person__reg { font-size: 12.5px; margin-top: 2px; margin-left: 14px; }

  .contacts {
    position: absolute;
    left: 70px; top: 262px;
    display: grid;
    grid-template-columns: 160px 230px;
    row-gap: 6px;
    font-size: 13px;
  }
  .contact { display: flex; align-items: center; gap: 8px; }
  .contact svg { width: 14px; height: 14px; flex: none; }

  .address {
    position: absolute;
    right: 44px; top: 198px;
    font-size: 13px;
    line-height: 1.45;
  }
  .band-charcoal {
    position: absolute;
    left: 0; bottom: 0;
    width: 67%; height: 22px;
    background: var(--charcoal);
  }
  .band-red {
    position: absolute;
    right: 0; bottom: 52px;
    width: 32%; height: 16px;
    background: var(--red);
  }
</style>
</head>
<body>

<section class="card card--back" aria-label="Card back">
  <div class="faint-disc"></div>
  <div class="brand">
    <span class="brand__name">lark funds</span>
    <span class="brand__dot"></span>
  </div>
  <div class="tagline">MONEY MADE FRIENDLY</div>
</section>

<section class="card card--front" aria-label="Card front">
  <div class="faint-disc"></div>
  <div class="brand">
    <span class="brand__name">lark funds</span>
    <span class="brand__dot"></span>
  </div>
  <div class="tagline">MONEY MADE FRIENDLY</div>

  <div class="person">
    <div class="person__name">CLARA DUNMORE<span class="person__creds">JP, Dip FS (FP), Dip FMBM</span></div>
    <div class="person__reg">ACRN:502761</div>
  </div>

  <div class="contacts">
    <div class="contact">
      <svg viewBox="0 0 16 16" fill="none" stroke="var(--red)" stroke-width="1.3"><circle cx="8" cy="8" r="7"/><path d="M5.5 4.8l1.3 1.4-.7 1.1a5 5 0 0 0 2.6 2.6l1.1-.7 1.4 1.3-.8 1a6 6 0 0 1-5.7-5.7z" fill="var(--red)" stroke="none"/></svg>
      <span>02 5550 1000</span>
    </div>
    <div class="contact">
      <svg viewBox="0 0 16 16" fill="none" stroke="var(--red)" stroke-width="1.3"><circle cx="8" cy="8" r="7"/><rect x="4.6" y="5.5" width="6.8" height="5" rx=".6" fill="var(--red)" stroke="none"/><path d="M4.8 5.8L8 8.4l3.2-2.6" stroke="var(--white)" stroke-width=".9"/></svg>
      <span>hello@larkfunds.com.au</span>
    </div>
    <div class="contact">
      <svg viewBox="0 0 16 16" fill="none" stroke="var(--red)" stroke-width="1.3"><circle cx="8" cy="8" r="7"/><rect x="5.6" y="4" width="4.8" height="8" rx="1" stroke-width="1.1"/></svg>
      <span>02 5550 1022</span>
    </div>
    <div class="contact">
      <svg viewBox="0 0 16 16" fill="none" stroke="var(--red)" stroke-width="1.1"><circle cx="8" cy="8" r="6.8"/><ellipse cx="8" cy="8" rx="3" ry="6.8"/><path d="M1.4 8h13.2M2.6 4.8h10.8M2.6 11.2h10.8"/></svg>
      <span>www.larkfunds.com.au</span>
    </div>
  </div>

  <div class="address">PO Box 1280<br>Harlow DC 2900</div>

  <div class="band-red"></div>
  <div class="band-charcoal"></div>
</section>

</body>
</html>
```